Security Warning Sign

We have an existing sign that needs an update. I have attached a picture of the current square sign. We need to maintain the same wording. It needs to be professional and appropriate to attach to our customers fence. Also attached is a copy of our building sign which may lend some inspiration and hopefully the ai format will assist. The final sign will be 600mm x 600mmOur website is www.halvorngate.com.au

```html
<!DOCTYPE html>
<html lang="en">
<head>
<meta charset="utf-8">
<title>Halvorngate Security Services – Surveillance Warning Sign</title>
<link rel="stylesheet" href="https://fonts.googleapis.com/css2?family=Montserrat:wght@700;800&family=Open+Sans:wght@700;800&display=swap">
<style>
  :root {
    --bg: #cccccc;
    --panel: #2b2b2b;
    --panel-deep: #1c1c1c;
    --white: #ffffff;
    --orange: #f28522;
    --ink: #2d2d2d;
  }
  * { margin: 0; padding: 0; box-sizing: border-box; }
  html, body { width: 1200px; height: 1200px; overflow: hidden; background: var(--bg); }
  .canvas { position: relative; width: 1200px; height: 1200px; }

  .sign {
    position: absolute; left: 87px; top: 87px; width: 1026px; height: 1026px;
    background: var(--white);
  }
  .top-strip { position: absolute; left: 0; top: 0; width: 100%; height: 33px; background: var(--panel); }

  .headline {
    position: absolute; left: 0; top: 33px; width: 100%; height: 168px;
    display: flex; align-items: center; justify-content: center;
    font-family: "Montserrat", sans-serif; font-weight: 800;
    font-size: 152px; letter-spacing: -3px; line-height: 1;
    color: var(--orange);
    text-shadow: 3px 4px 6px rgba(0,0,0,0.35);
    padding-top: 6px;
  }

  .message-panel {
    position: absolute; left: 0; top: 201px; width: 100%; height: 600px;
    background: var(--panel); overflow: hidden;
  }
  .camera-visual {
    position: absolute; right: 0; top: 80px; width: 440px; height: 520px;
    background: radial-gradient(ellipse at 45% 45%, #5a5a5a 0%, #3a3232 30%, #2b2b2b 70%);
    opacity: 0.8;
  }
  .message {
    position: absolute; left: 0; top: 68px; width: 100%;
    text-align: center;
    font-family: "Montserrat", sans-serif; font-weight: 800;
    font-size: 70px; line-height: 100px; color: var(--white);
    text-shadow: 3px 4px 6px rgba(0,0,0,0.6);
    padding-right: 14px;
  }

  .footer { position: absolute; left: 0; top: 801px; width: 100%; height: 225px; }
  .brand { position: absolute; left: 31px; top: 32px; display: flex; align-items: center; gap: 20px; }
  .brand-mark { width: 168px; height: 168px; border-radius: 50%; background: var(--orange); }
  .brand-name {
    font-family: "Open Sans", sans-serif; font-weight: 800;
    font-size: 40px; line-height: 43px; color: var(--ink); letter-spacing: 0.3px;
  }
  .website {
    position: absolute; left: 556px; top: 55px;
    font-family: "Open Sans", sans-serif; font-weight: 800;
    font-size: 21px; color: var(--ink);
  }
  .phone-bar { position: absolute; left: 500px; top: 100px; width: 526px; height: 81px; }
  .phone-bar svg { position: absolute; left: 0; top: 0; }
  .phone-number {
    position: absolute; left: 148px; top: 0; height: 81px;
    display: flex; align-items: center;
    font-family: "Open Sans", sans-serif; font-weight: 800;
    font-size: 50px; color: var(--white); letter-spacing: 0.5px;
  }
</style>
</head>
<body>
<div class="canvas">
  <div class="sign">
    <div class="top-strip"></div>
    <div class="headline">WARNING</div>

    <div class="message-panel">
      <div class="camera-visual" role="img" aria-label="Faded photograph of a CCTV security camera"></div>
      <p class="message">ELECTRONIC<br>SURVEILLANCE<br>AND RECORDING<br>DEVICES INSTALLED<br>IN THIS AREA</p>
    </div>

    <div class="footer">
      <div class="brand">
        <div class="brand-mark"></div>
        <div class="brand-name">HALVORNGATE<br>SECURITY<br>SERVICES</div>
      </div>
      <div class="website">WWW.HALVORNGATE.COM.AU</div>
      <div class="phone-bar">
        <svg width="526" height="81" viewBox="0 0 526 81">
          <polygon points="22,81 52,0 60,0 30,81" fill="var(--orange)"/>
          <polygon points="52,81 82,0 526,0 526,81" fill="var(--orange)"/>
          <g transform="translate(82,14)" fill="var(--ink)">
            <path d="M10 12 C6 16 6 22 10 30 C16 42 26 50 36 54 C42 56 46 54 48 50 L50 46 L40 38 L34 43 C28 40 22 34 19 28 L24 22 L17 11 Z"/>
            <path d="M28 12 A16 16 0 0 1 44 28" fill="none" stroke="var(--ink)" stroke-width="4"/>
            <path d="M30 2 A26 26 0 0 1 54 26" fill="none" stroke="var(--ink)" stroke-width="4"/>
          </g>
        </svg>
        <div class="phone-number">1300 555 014</div>
      </div>
    </div>
  </div>
</div>
</body>
</html>
```